Design The Loomfield Hompage

See powerpoint

Industry/Entity Type

SAAS data product

Coding

Coded - Design and coding required

Number of Pages Required

4 page

Font styles to use
Sans Serif

```html
<!DOCTYPE html>
<html lang="en">
<head>
<meta charset="utf-8">
<title>The Loomfield — Public Data Made Easy</title>
<link href="https://fonts.googleapis.com/css2?family=Poppins:wght@300;400;500;600;700&display=swap" rel="stylesheet">
<style>
:root{
  --ink:#1e2538;
  --body:#4a5062;
  --blue:#2a44df;
  --violet:#5a14f1;
  --white:#ffffff;
  --footer-a:#f7f4f2;
  --footer-b:#e4e8f2;
  --line:#c9ccd6;
}
*{margin:0;padding:0;box-sizing:border-box}
html,body{width:726px;height:1200px;overflow:hidden}
body{font-family:"Poppins",sans-serif;color:var(--ink);background:var(--white);position:relative}
.abs{position:absolute}
.swoosh{position:absolute;left:0;top:0}
.brand{position:absolute;display:flex;align-items:center;gap:5px;font-weight:600;color:var(--blue)}
.brand .dot{width:10px;height:10px;border-radius:50%;background:var(--blue)}
.brand--top{left:54px;top:30px;font-size:14px}
.brand--foot{left:73px;top:1025px;font-size:17px}
.nav{position:absolute;top:33px;left:312px;display:flex;font-size:7.6px;font-weight:600;color:var(--white)}
.nav a{color:inherit;text-decoration:none;position:absolute;white-space:nowrap}
.btn{position:absolute;border-radius:14px;font-weight:600;display:flex;align-items:center;justify-content:center;font-size:7.8px;white-space:nowrap}
.btn--signup{left:531px;top:26px;width:68px;height:27px;background:var(--white);color:var(--ink)}
.btn--login{left:604px;top:26px;width:67px;height:27px;border:1.3px solid var(--white);color:var(--white)}
.hero-title{position:absolute;left:52px;top:136px;font-size:41px;line-height:42px;font-weight:700;letter-spacing:-.3px}
.hero-text{position:absolute;left:53px;width:250px;font-size:8px;line-height:13.5px;font-weight:300;color:var(--body)}
.btn--register{left:55px;top:331px;width:159px;height:27px;background:linear-gradient(90deg,var(--blue),var(--violet));color:var(--white)}
.btn--pricing{left:220px;top:331px;width:68px;height:27px;border:1.3px solid var(--ink);color:var(--ink)}
.hero-art{position:absolute;left:328px;top:78px;width:366px;height:317px;border-radius:14px;background:linear-gradient(135deg,#f1f3f8 0%,#dfe6fb 55%,#f0e4da 100%)}
.section-title{position:absolute;left:0;width:726px;top:428px;text-align:center;font-size:21.5px;line-height:27px;font-weight:600}
.section-lead{position:absolute;left:163px;width:400px;top:490px;text-align:center;font-size:8.6px;line-height:13.5px;font-weight:300;color:var(--body)}
.feature{position:absolute;width:190px;text-align:center}
.feature .icon{width:44px;height:44px;margin:0 auto 20px;border-radius:10px;background:linear-gradient(135deg,#e6e9f6,#d8defa)}
.feature h3{font-size:11.3px;font-weight:600;margin-bottom:6px}
.feature p{font-size:8.2px;line-height:13.5px;font-weight:300;color:var(--body)}
.wave{position:absolute;left:0;top:870px}
.foot-about{position:absolute;left:73px;top:1081px;width:170px;font-size:8.4px;line-height:13.5px;font-weight:300;color:var(--body)}
.foot-col{position:absolute;top:1003px}
.foot-col h4{font-size:11px;font-weight:600;margin-bottom:12px}
.foot-col li{list-style:none;font-size:8.2px;font-weight:300;color:var(--body);line-height:16px}
.contact-row{display:flex;gap:6px;font-size:8.2px;font-weight:300;color:var(--body);line-height:11.5px}
.mail{width:11px;height:8px;margin-top:2px;flex:none}
.social{position:absolute;top:1071px;width:23px;height:23px;border-radius:50%;border:1.2px solid var(--ink)}
.divider{position:absolute;left:54px;top:1161px;width:618px;height:1px;background:var(--line)}
.copyright{position:absolute;left:0;width:726px;top:1175px;text-align:center;font-size:8px;color:var(--body)}
.to-top{position:absolute;left:688px;top:1150px;width:24px;height:24px;border-radius:50%;background:linear-gradient(135deg,var(--blue),var(--violet));display:flex;align-items:center;justify-content:center}
</style>
</head>
<body>

<svg class="swoosh" width="726" height="290" viewBox="0 0 726 290" aria-hidden="true">
  <defs>
    <linearGradient id="swooshFill" x1="0" y1="0" x2="1" y2="0">
      <stop offset="0" stop-color="#1f4fd8"/>
      <stop offset="1" stop-color="#5b14f0"/>
    </linearGradient>
  </defs>
  <path d="M184,0 C225,70 360,104 500,104 C630,104 700,190 726,276 L726,0 Z" fill="url(#swooshFill)"/>
</svg>

<div class="brand brand--top"><span class="dot"></span>The Loomfield</div>

<nav class="nav">
  <a style="left:0">PRICING</a>
  <a style="left:53px">DOCUMENTATION</a>
  <a style="left:142px">DATA</a>
  <a style="left:184px">BLOG</a>
</nav>
<a class="btn btn--signup">SIGNUP</a>
<a class="btn btn--login">LOGIN</a>

<h1 class="hero-title">Public Data<br>Made Easy</h1>
<p class="hero-text" style="top:239px">From demographics to economics, from weather to health, on country level or community level. The Loomfield collects many public data sources and organizes it for you.</p>
<p class="hero-text" style="top:288px">Use The Loomfield API or SDK to easily get public data from many different sources.</p>
<a class="btn btn--register">REGISTER AND START FOR FREE</a>
<a class="btn btn--pricing">PRICING</a>

<div class="hero-art" role="img" aria-label="Illustration of people working with data dashboards, charts and a computer desk"></div>

<h2 class="section-title">Designed for Developers<br>In Need of Data</h2>
<p class="section-lead">As a data scientist or engineer you always are looking for getting more data in with more efficiency. This is exactly what The Loomfield is making possible for you.</p>

<div class="feature" style="left:50px;top:540px">
  <div class="icon" role="img" aria-label="API and gear icon"></div>
  <h3>Many Sources</h3>
  <p>Public data comes from many sources, all with their own data format &amp; interface. No longer worry about these differences, The Loomfield collects &amp; standardizes it for you.</p>
</div>
<div class="feature" style="left:268px;top:540px">
  <div class="icon" role="img" aria-label="Monitor with gears icon"></div>
  <h3>Integrate</h3>
  <p>Use the loomfield API to combine Public data with your own comapny data and create value for your business.</p>
</div>
<div class="feature" style="left:488px;top:540px">
  <div class="icon" role="img" aria-label="Globe with location pin icon"></div>
  <h3>Regional</h3>
  <p>Do you need regional information in your pipeline ? The loomfield provides public data up to community level.</p>
</div>
<div class="feature" style="left:50px;top:705px">
  <div class="icon" role="img" aria-label="Processor chip with gear icon"></div>
  <h3>Automate</h3>
  <p>Use the latest public data in your data pipeline as the loomfield makes daily updates to the data. You no longer need to worry about multiple differnt data sources.</p>
</div>
<div class="feature" style="left:268px;top:705px">
  <div class="icon" role="img" aria-label="SDK package box icon"></div>
  <h3>The Loomfield SDK</h3>
  <p>Use our SDK to access our data without any knowledge of our API.</p>
</div>
<div class="feature" style="left:488px;top:705px">
  <div class="icon" role="img" aria-label="Document with magnifying glass icon"></div>
  <h3>Tracable</h3>
  <p>For all data we give you the legends as well as the sources from which we retrieve the data. So you always know what the data is exactly about.</p>
</div>

<svg class="wave" width="726" height="330" viewBox="0 0 726 330" aria-hidden="true">
  <defs>
    <linearGradient id="footFill" x1="0" y1="0" x2="1" y2="1">
      <stop offset="0" stop-color="#f8f4f1"/>
      <stop offset="1" stop-color="#e2e7f2"/>
    </linearGradient>
  </defs>
  <path d="M0,80 C60,20 150,5 230,8 C340,12 430,100 540,100 C620,100 680,60 726,28 L726,330 L0,330 Z" fill="url(#footFill)"/>
</svg>

<div class="brand brand--foot"><span class="dot"></span>The Loomfield</div>
<p class="foot-about">The Loomfield was created to simplify access to public data and save you countless hours of manual collection</p>

<div class="foot-col" style="left:263px">
  <h4>Our Product</h4>
  <ul><li>Introduction</li><li>The datamodels</li><li>The API</li><li>The SDK</li></ul>
</div>
<div class="foot-col" style="left:388px">
  <h4>The Company</h4>
  <ul><li>About</li><li>Frequently Asked Questions</li><li>Privacy Policy</li><li>Cookie Policy</li><li>Terms of Service</li></ul>
</div>
<div class="foot-col" style="left:540px">
  <h4>Contact Us</h4>
  <div class="contact-row">
    <svg class="mail" viewBox="0 0 11 8" aria-hidden="true"><rect width="11" height="8" rx="1" fill="#2a44df"/><path d="M0.5,0.8 L5.5,4.6 L10.5,0.8" stroke="#fff" stroke-width="1" fill="none"/></svg>
    <span>Email:<br>info@loomfield-hq.io</span>
  </div>
</div>
<a class="social" style="left:540px" aria-label="Social link 1"></a>
<a class="social" style="left:567px" aria-label="Social link 2"></a>

<div class="divider"></div>
<p class="copyright">© 2024 The Loomfield. All rights reserved.</p>
<a class="to-top" aria-label="Back to top">
  <svg width="8" height="6" viewBox="0 0 8 6" aria-hidden="true"><path d="M1,4.5 L4,1.5 L7,4.5" stroke="#fff" stroke-width="1.3" fill="none"/></svg>
</a>

</body>
</html>
```